Kneadwell Bodycare Studio

We are a Massage Therapy business based in Invercargill, New Zealand. We specialise in Sports and deep tissue massage but also provide relaxation and aromatherapy massage. We would like to see designs that use the the logo.
The final design should promote health and fitness.
Updates

Hi I am getting feedback that my business card picture is poor quality. I got this picture from brightpress under massage. So if you google this image a better quality picture should come up,. If not hope to upload a better image by tomorow, thanks.

Target Market(s)

Sports, people with pain and injuries

Industry/Entity Type

Massage

Requirements
Must have
• Logo, muscle body that is used on the business card, also a poster that matches my business card
Nice to have
• Picture of muscle man, shown on my business card
Should not have
• Not a picture of a real person

```html
<!DOCTYPE html>
<html lang="en">
<head>
<meta charset="utf-8">
<title>Kneadwell Bodycare Studio – Are you in pain?</title>
<link rel="stylesheet" href="https://fonts.googleapis.com/css2?family=Archivo+Black&family=PT+Sans:wght@700&display=swap">
<style>
  :root {
    --paper: #faf8f5;
    --ink: #0b0b0b;
    --blue: #0aa8e6;
    --white: #ffffff;
    --grey-light: #e9e8e6;
  }
  * { margin: 0; padding: 0; box-sizing: border-box; }
  html, body { width: 1040px; height: 1200px; overflow: hidden; background: var(--paper); }
  .flyer { position: relative; width: 1040px; height: 1200px; background: var(--paper); overflow: hidden; font-family: "PT Sans", Arial, sans-serif; font-weight: 700; }
  h1, h2 { font-weight: 700; }

  .anatomy-art {
    position: absolute; left: 0; top: 0; width: 640px; height: 660px;
    background: radial-gradient(ellipse at 35% 40%, #9a9a9a 0%, #c4c4c4 40%, var(--grey-light) 68%, rgba(250,248,245,0) 100%);
  }

  .headline-lead {
    position: absolute; right: 92px; top: 112px;
    font-family: "Archivo Black", Arial, sans-serif; font-weight: 400; font-size: 86px; line-height: 1;
    color: var(--ink);
  }
  .headline-main {
    position: absolute; right: 86px; top: 220px;
    font-family: "Archivo Black", Arial, sans-serif; font-weight: 400; font-size: 240px; line-height: 1;
    color: var(--blue); -webkit-text-stroke: 5px var(--ink); paint-order: stroke fill;
    letter-spacing: -10px;
  }

  .services { position: absolute; left: 102px; top: 660px; list-style: none; }
  .services li, .price-row {
    display: flex; align-items: center; font-size: 28px; color: var(--ink);
    letter-spacing: 1.5px; height: 40px; line-height: 40px;
  }
  .services li { margin-bottom: 9px; }
  .services li::before, .price-row::before {
    content: ""; width: 19px; height: 19px; border-radius: 50%;
    background: var(--blue); margin-right: 8px; flex: none;
  }

  .prices-title { position: absolute; left: 622px; top: 662px; font-size: 28px; line-height: 36px; color: var(--blue); letter-spacing: 2px; }
  .price-row { position: absolute; left: 598px; }
  .price-row.r1 { top: 708px; } .price-row.r2 { top: 762px; } .price-row.r3 { top: 816px; }
  .price-tag {
    position: absolute; left: 826px; width: 136px; height: 42px;
    background: var(--blue); transform: skewX(-14deg);
  }
  .price-tag span {
    display: block; transform: skewX(14deg); text-align: center;
    color: var(--white); font-size: 40px; line-height: 42px; letter-spacing: 1px;
  }
  .price-tag.r1 { top: 707px; } .price-tag.r2 { top: 761px; } .price-tag.r3 { top: 815px; }
  .price-rule { position: absolute; left: 958px; width: 82px; height: 6px; background: var(--blue); }
  .price-rule.r1 { top: 725px; } .price-rule.r2 { top: 779px; } .price-rule.r3 { top: 833px; }

  .contact-band { position: absolute; left: 0; top: 893px; width: 1040px; height: 134px; background: var(--ink); }
  .brand { position: absolute; left: 92px; top: 54px; display: flex; align-items: center; gap: 10px; }
  .brand-dot { width: 12px; height: 12px; border-radius: 50%; background: var(--blue); }
  .brand-name { color: var(--blue); font-size: 29px; line-height: 36px; }

  .contact-line { position: absolute; right: 94px; display: flex; align-items: center; gap: 6px; color: var(--white); white-space: nowrap; }
  .contact-address { top: 14px; font-size: 17px; line-height: 24px; letter-spacing: 0.5px; }
  .contact-phone { top: 36px; font-size: 36px; line-height: 40px; letter-spacing: 3px; }
  .contact-icon { width: 24px; height: 24px; flex: none; }
  .contact-phone .contact-icon { width: 26px; height: 26px; }
  .therapist { position: absolute; right: 94px; top: 76px; color: var(--blue); font-size: 34px; line-height: 36px; letter-spacing: 3px; }
  .credential { position: absolute; right: 94px; top: 111px; color: var(--white); font-size: 16px; line-height: 20px; letter-spacing: 0.5px; white-space: nowrap; }

  .band-rule { position: absolute; left: 0; top: 1027px; width: 1040px; height: 8px; background: var(--blue); }
  .photo-strip { position: absolute; left: 0; top: 1037px; width: 1040px; height: 133px; }
  .photo { position: absolute; top: 0; height: 133px; }
  .photo.p1 { left: 0; width: 162px; background: linear-gradient(135deg, #e7b28a, #b5714a); }
  .photo.p2 { left: 175px; width: 218px; background: linear-gradient(135deg, #f1e8e2, #3a3a3a 60%, #d8b39a); }
  .photo.p3 { left: 407px; width: 191px; background: linear-gradient(180deg, #b9cfd6, #7e9ba4 60%, #e9e2da); }
  .photo.p4 { left: 611px; width: 216px; background: linear-gradient(135deg, #8a3a20, #d9965f 55%, #5a1e12); }
  .photo.p5 { left: 840px; width: 200px; background: linear-gradient(180deg, #f5f1ee, #c9987b 60%, #f2ece8); }
  .footer-band { position: absolute; left: 0; top: 1171px; width: 1040px; height: 29px; background: var(--blue); }
</style>
</head>
<body>
<main class="flyer">
  <div class="anatomy-art" role="img" aria-label="Greyscale anatomical illustration of back and shoulder muscles with highlighted pain points"></div>

  <h1>
    <span class="headline-lead">Are you in</span>
    <span class="headline-main">PAIN?</span>
  </h1>

  <ul class="services">
    <li>Deep Tissue</li>
    <li>Sports Massage</li>
    <li>Relaxation</li>
    <li>Aromatherapy</li>
    <li>Hot Stones</li>
  </ul>

  <section class="prices">
    <h2 class="prices-title">PRICES</h2>
    <div class="price-row r1">30 minutes</div>
    <div class="price-row r2">60 minutes</div>
    <div class="price-row r3">90 minutes</div>
    <div class="price-tag r1"><span>$40</span></div>
    <div class="price-tag r2"><span>$60</span></div>
    <div class="price-tag r3"><span>$80</span></div>
    <div class="price-rule r1"></div>
    <div class="price-rule r2"></div>
    <div class="price-rule r3"></div>
  </section>

  <footer class="contact-band">
    <div class="brand">
      <span class="brand-dot"></span>
      <span class="brand-name">Kneadwell Bodycare Studio</span>
    </div>
    <div class="contact-line contact-address">
      <svg class="contact-icon" viewBox="0 0 24 24" aria-hidden="true"><circle cx="12" cy="12" r="12" fill="#0aa8e6"/><path d="M6 12 L12 6.5 L18 12 H16 V17.5 H8 V12 Z" fill="#fff"/></svg>
      18 Harlow St, Invercargill 9810
    </div>
    <div class="contact-line contact-phone">
      <svg class="contact-icon" viewBox="0 0 24 24" aria-hidden="true"><circle cx="12" cy="12" r="12" fill="#0aa8e6"/><path d="M8 6.5c.6-.4 1.3-.3 1.6.3l1 2c.3.5.1 1.1-.3 1.4l-.8.6c.6 1.4 1.6 2.5 3 3.1l.6-.8c.4-.4 1-.6 1.5-.3l2 1c.6.3.7 1 .3 1.6l-.8 1c-.5.6-1.3.8-2 .5C10.6 15.4 8.6 13.4 7.1 10c-.3-.7-.1-1.5.5-2z" fill="#fff"/></svg>
      0275550142
    </div>
    <div class="therapist">MAREN HOLT</div>
    <div class="credential">Bachelor Therapeutic &amp; Sports Massage</div>
  </footer>

  <div class="band-rule"></div>
  <div class="photo-strip">
    <div class="photo p1" role="img" aria-label="Hands massaging a shoulder"></div>
    <div class="photo p2" role="img" aria-label="Therapist stretching an athlete's leg"></div>
    <div class="photo p3" role="img" aria-label="Meditation pose by the sea"></div>
    <div class="photo p4" role="img" aria-label="Aromatherapy back massage with rose petals"></div>
    <div class="photo p5" role="img" aria-label="Hot stone massage on a client's back"></div>
  </div>
  <div class="footer-band"></div>
</main>
</body>
</html>
```